Invitation Design Project

We are a printing company that offers personalized cards for different family occasions. We would like you to design 2 amazing cards for us: Christmas card and Birth Announcement for a boy.

1. Christmas Card
• Theme for the Christmas card: Santa Claus.
• No preference when it comes to colours.
• May contain 1-2 images of a family, incorporated into the layout in a creative way. You will find the images of the family attached to this brief.
• Format of the card: folded, landscape after folding. Size with Bleed: 218 x 156 mm. Size without Bleed: 210 x 148 mm
• Text on the card: generic Christmas text common in your culture (in English).

2. Birth Announcement for a Boy
• The design has to be done in bright and vivid colours;
• The design has to contain one image of a baby. You will find the image of the baby attached to the brief;
• Design elements: nice baby objects, toys or a big cute teddy bear
• Format: flat horizontal double sided card. Size with Bleed: 113 x 156 mm. Size without Bleed: 105 x 148 mm
• Text: put text that is common for a birth announcement.

We look forward to hearing from you. Please do not hesitate to contact me if you have any questions about anything.

Reason: few designs received

Target Market(s)

Families

Industry/Entity Type

Landscape

Requirements
Must have
• • Cards need to be designed for printing purposes.
Should not have
• • No stock photography or stock illustrations can be used as static design elements. All the elements should be created by you.
• Images cannot be other form than square and rectangular and they cannot be tilted
• No words (text) can be a static part of a design.

```html
<!DOCTYPE html>
<html lang="en">
<head>
<meta charset="utf-8">
<title>Santa Belt Christmas Card</title>
<link href="https://fonts.googleapis.com/css2?family=Oswald:wght@600&family=Open+Sans:ital,wght@0,300;1,400&family=Lora:ital,wght@1,400&display=swap" rel="stylesheet">
<style>
  :root {
    --santa-red: #a11527;
    --belt-black: #050505;
    --snow-white: #ffffff;
    --photo-light: #f6f3ef;
    --photo-skin: #e6bf9f;
    --photo-blue: #aebfcf;
  }
  html, body {
    margin: 0;
    padding: 0;
    overflow: hidden;
    background: var(--santa-red);
  }
  .card {
    position: relative;
    width: 869px;
    height: 1200px;
    background: var(--santa-red);
    overflow: hidden;
  }
  .photo-cloud {
    position: absolute;
    left: 0;
    top: 0;
    width: 869px;
    height: 680px;
  }
  .greeting {
    position: absolute;
    left: 0;
    top: 698px;
    width: 100%;
    text-align: center;
    color: var(--snow-white);
  }
  .greeting-shout {
    margin: 0;
    font-family: "Oswald", sans-serif;
    font-weight: 600;
    font-size: 40px;
    line-height: 50px;
    letter-spacing: 1px;
  }
  .greeting-line {
    margin: 0;
    font-family: "Open Sans", sans-serif;
    font-weight: 300;
    font-size: 31px;
    line-height: 42px;
  }
  .greeting-script {
    margin: 0;
    font-family: "Lora", serif;
    font-style: italic;
    font-size: 47px;
    line-height: 58px;
  }
  .belt {
    position: absolute;
    left: 0;
    top: 879px;
    width: 869px;
    height: 233px;
    background: var(--belt-black);
  }
  .belt-hole {
    position: absolute;
    top: 971px;
    width: 44px;
    height: 44px;
    border-radius: 50%;
    background: var(--snow-white);
  }
  .buckle {
    position: absolute;
    left: 240px;
    top: 859px;
    width: 422px;
    height: 270px;
    box-sizing: border-box;
    border: 10px solid var(--snow-white);
    background: var(--belt-black);
    color: var(--snow-white);
    text-align: center;
    padding-top: 57px;
  }
  .family-name {
    margin: 0 0 4px;
    font-family: "Open Sans", sans-serif;
    font-style: italic;
    font-size: 42px;
    line-height: 52px;
  }
  .family-members {
    margin: 0;
    font-family: "Lora", serif;
    font-style: italic;
    font-size: 36px;
    line-height: 41px;
  }
</style>
</head>
<body>
<main class="card">
  <svg class="photo-cloud" viewBox="0 0 869 680" xmlns="http://www.w3.org/2000/svg">
    <defs>
      <linearGradient id="familyTones" gradientUnits="userSpaceOnUse" x1="0" y1="0" x2="0" y2="620">
        <stop offset="0%" stop-color="var(--photo-light)"/>
        <stop offset="30%" stop-color="#f0dccb"/>
        <stop offset="55%" stop-color="var(--photo-skin)"/>
        <stop offset="78%" stop-color="#f2e6dc"/>
        <stop offset="100%" stop-color="var(--photo-blue)"/>
      </linearGradient>
      <clipPath id="photoScallop">
        <circle cx="435" cy="250" r="265"/>
        <circle cx="435" cy="550" r="62"/><circle cx="259" cy="493" r="62"/>
        <circle cx="150" cy="343" r="62"/><circle cx="150" cy="157" r="62"/>
        <circle cx="259" cy="7" r="62"/><circle cx="435" cy="-50" r="62"/>
        <circle cx="611" cy="7" r="62"/><circle cx="720" cy="157" r="62"/>
        <circle cx="720" cy="343" r="62"/><circle cx="611" cy="493" r="62"/>
      </clipPath>
    </defs>
    <g class="cloud-frame" fill="var(--snow-white)">
      <circle cx="435" cy="250" r="300"/>
      <circle cx="435" cy="550" r="100"/><circle cx="259" cy="493" r="100"/>
      <circle cx="150" cy="343" r="100"/><circle cx="150" cy="157" r="100"/>
      <circle cx="259" cy="7" r="100"/><circle cx="435" cy="-50" r="100"/>
      <circle cx="611" cy="7" r="100"/><circle cx="720" cy="157" r="100"/>
      <circle cx="720" cy="343" r="100"/><circle cx="611" cy="493" r="100"/>
    </g>
    <rect class="family-photo" role="img" aria-label="Family photo: parents and two children huddled together smiling down at the camera" x="0" y="0" width="869" height="680" fill="url(#familyTones)" clip-path="url(#photoScallop)"/>
  </svg>

  <section class="greeting">
    <p class="greeting-shout">HO. HO. HO.</p>
    <p class="greeting-line">WISHING YOU A SEASON</p>
    <p class="greeting-script">filled with love and laughter</p>
  </section>

  <div class="belt"></div>
  <span class="belt-hole" style="left:44px"></span>
  <span class="belt-hole" style="left:152px"></span>
  <span class="belt-hole" style="left:691px"></span>
  <span class="belt-hole" style="left:800px"></span>

  <section class="buckle">
    <p class="family-name">The Hollis Family</p>
    <p class="family-members">Evan, Marisa,</p>
    <p class="family-members">Tilly &amp; Owen</p>
  </section>
</main>
</body>
</html>
```